Marnick Building Materials letterhead template

Simple but professional letterhead template for business communication.
LOGO/name in upper left, balanced by company contact info on right upper.
Subject description, date...
addressee, cc: and BC: if applicable editable info..

Need extra days to review

```html
<!DOCTYPE html>
<html lang="en">
<head>
<meta charset="utf-8">
<title>Marnick Building Materials – Letterhead</title>
<link rel="stylesheet" href="https://fonts.googleapis.com/css2?family=Didact+Gothic&family=Roboto:wght@400;700&display=swap">
<style>
  :root {
    --brand-blue: #0a5bc4;
    --paper-light: #ececec;
    --paper-dark: #d5d5d5;
    --body-text: #575757;
    --footer-text: #ffffff;
  }
  * { margin: 0; padding: 0; box-sizing: border-box; }
  html, body {
    width: 1023px;
    height: 1200px;
    overflow: hidden;
  }
  body {
    background: var(--paper-dark);
  }
  .letterhead {
    position: relative;
    width: 1023px;
    height: 1200px;
    background: linear-gradient(100deg, var(--paper-light) 0%, #dedede 55%, var(--paper-dark) 100%);
    font-family: "Didact Gothic", "Century Gothic", sans-serif;
    color: var(--body-text);
  }
  .brand {
    position: absolute;
    top: 74px;
    left: 0;
    right: 0;
    display: flex;
    justify-content: center;
    align-items: center;
    gap: 14px;
  }
  .brand-square {
    width: 80px;
    height: 80px;
    border-radius: 14px;
    background: var(--brand-blue);
  }
  .brand-name {
    font-family: "Roboto", sans-serif;
    font-weight: 700;
    font-size: 22px;
    line-height: 27px;
    letter-spacing: 1.6px;
    text-transform: uppercase;
    color: var(--brand-blue);
  }
  .letter {
    position: absolute;
    top: 310px;
    left: 97px;
    right: 86px;
  }
  .salutation {
    font-size: 17px;
    margin-bottom: 36px;
  }
  .letter p {
    font-size: 13.4px;
    line-height: 18px;
    text-align: justify;
    margin-bottom: 18px;
  }
  .letter p.spaced { margin-top: 36px; }
  .closing {
    font-size: 13.4px;
    margin-top: 72px;
  }
  .contact-bar {
    position: absolute;
    left: 0;
    right: 0;
    bottom: 0;
    height: 26px;
    background: var(--brand-blue);
    color: var(--footer-text);
    font-family: "Roboto", sans-serif;
    font-size: 13px;
    display: flex;
    align-items: center;
    justify-content: center;
    gap: 20px;
  }
  .contact-item {
    display: flex;
    align-items: center;
    gap: 7px;
    white-space: nowrap;
  }
  .contact-item svg { width: 12px; height: 12px; fill: var(--footer-text); }
</style>
</head>
<body>
<main class="letterhead">
  <header class="brand">
    <div class="brand-square"></div>
    <div class="brand-name">Marnick<br>Building<br>Materials</div>
  </header>

  <section class="letter">
    <p class="salutation">Dear John,</p>
    <p>Donec malesuada orci vitae nulla accumsan porta a id massa. Quisque accumsan iaculis magna sit amet fringilla. Maecenas consequat, magna eget tincidunt semper, odio nibh rutrum mi, id feugiat ante nisi eu risus. Vestibulum nunc orci, rhoncus a placerat in, ultricies in mi. Cras mattis varius eros, vel fringilla nisi suscipit eget. Quisque scelerisque sagittis nulla at porttitor.</p>
    <p>Lorem ipsum dolor sit amet, consectetur adipiscing elit. Donec orci purus, luctus vitae dignissim eu, iaculis sed purus. Vivamus faucibus, ipsum nec aliquet viverra, leo mauris condimentum ligula, sit amet sagittis enim ligula quis arcu. Nam egestas tortor id nisi porttitor mattis. In tortor ante, ultricies in suscipit a, tempus non massa. Vivamus et auctor mi. Fusce vel massa nulla. Phasellus nec eros mauris, et scelerisque orci.</p>
    <p class="spaced">It is a long established fact that a reader will be distracted by the readable content of a page when looking at its layout. The point of using Lorem Ipsum is that it has a more-or-less normal distribution of letters, as opposed to using 'Content here, content here', making it look like readable English. Many desktop publishing packages</p>
    <p>Sed id augue vitae urna euismod commodo aliquet a quam. Pellentesque arcu velit, cursus et malesuada ut, consequat et diam. Nullam erat sem, rhoncus id ullamcorper vitae, rhoncus et arcu. In ultricies ultricies nulla, ut rutrum nisi iaculis at. Donec eu magna a metus ornare faucibus. Fusce aliquet faucibus ultricies. Morbi semper, est id tincidunt gravida, sem arcu adipiscing lacus, ac bibendum nulla leo eu purus. Quisque nec diam sed risus consectetur a ccumsan quis quis nibh. Vestibulum id purus lorem.</p>
    <p class="closing">Sincerely,</p>
  </section>

  <footer class="contact-bar">
    <span class="contact-item">PO Box 318 Harlow Ridge, North Dakota 58411</span>
    <span class="contact-item">
      <svg viewBox="0 0 24 24" aria-hidden="true"><path d="M6.6 10.8a15.1 15.1 0 0 0 6.6 6.6l2.2-2.2a1 1 0 0 1 1-.25 11.4 11.4 0 0 0 3.6.57 1 1 0 0 1 1 1V20a1 1 0 0 1-1 1A17 17 0 0 1 3 4a1 1 0 0 1 1-1h3.5a1 1 0 0 1 1 1c0 1.25.2 2.45.57 3.57a1 1 0 0 1-.25 1z"/></svg>
      (555) 204.6813
    </span>
    <span class="contact-item">
      <svg viewBox="0 0 24 24" aria-hidden="true"><path d="M2 5h20v14H2z M2 5l10 8 10-8" /></svg>
      info@marnickbuildingmaterials
    </span>
    <span class="contact-item">
      <svg viewBox="0 0 24 24" aria-hidden="true"><path d="M12 2a10 10 0 1 0 0 20 10 10 0 0 0 0-20zm0 2.2a7.8 7.8 0 0 1 5.6 2.4l-2.4 1.2-1.6-.8-1.4 1.6.8 2-2.6 1.4-1.4 2.6 1.2 3.2A7.8 7.8 0 0 1 6 6.8l2 1.4 2-2.2-.6-1.4A7.8 7.8 0 0 1 12 4.2z"/></svg>
      www.marnickbuildingmaterials
    </span>
  </footer>
</main>
</body>
</html>
```